Design a label for a dog shampoo names furbloom, the sell point of this series of shampoo is “just like wash your dogs with milk, not harm for your hand ”, the style could be gentle or professional or even amazing.

Use only 2 colors in the design job, the color of our logo could be changed, it depends on your whole page. Please design in CDR or ai.

update:
Pls do more change with the fonts when you design the front page, including title and details. Try more styles of fonts. Addition, this design will be printed on the bottle, no a label stick on it.
Updates

Do not put a real dog or animal on the page, Pay more attention to the types of fonts

Reason: Expect for more design idea.

Target Market(s)

people 20-30 years old who have dogs and cats at home

Industry/Entity Type

It Professional

Requirements
Nice to have
• It would be nice if you add some detail words in the design of the right side.

```html
<!DOCTYPE html>
<html lang="en">
<head>
<meta charset="utf-8">
<title>furbloom Milk Shampoo – Bottle Print</title>
<link href="https://fonts.googleapis.com/css2?family=Roboto+Condensed:wght@400;700&family=Alfa+Slab+One&display=swap" rel="stylesheet">
<style>
  :root{
    --teal:#23a9bd;
    --teal-dark:#1a8fa3;
    --magenta:#b94c9f;
    --white:#ffffff;
    --print-base:#f7f7f5;
    --stage:#e4e4e4;
    --ink-soft:#2a9fb2;
  }
  *{box-sizing:border-box;margin:0;padding:0}
  html,body{width:1200px;height:1200px;overflow:hidden}
  body{
    background:var(--stage);
    font-family:"Roboto Condensed",Arial,sans-serif;
    display:flex;align-items:center;justify-content:center;gap:60px;
  }
  .print-area{
    width:500px;height:960px;background:var(--print-base);
    border-radius:24px;position:relative;
    box-shadow:0 2px 10px rgba(0,0,0,.08);
  }

  /* ---------- brand mark ---------- */
  .brand{
    display:flex;align-items:center;justify-content:center;gap:12px;
    color:var(--teal);font-weight:700;letter-spacing:1px;
  }
  .brand-dot{border-radius:50%;background:var(--teal)}
  .front .brand{position:absolute;top:150px;left:0;right:0;font-size:64px}
  .front .brand-dot{width:22px;height:22px}
  .back .brand{margin-top:90px;font-size:40px}
  .back .brand-dot{width:14px;height:14px}

  /* ---------- front panel ---------- */
  .scroll-frame{
    position:absolute;left:50px;top:270px;width:400px;height:560px;
    background:var(--magenta);border-radius:28px;
  }
  .front-copy{
    position:absolute;left:90px;top:330px;width:320px;text-align:center;color:var(--white);
  }
  .claim{font-weight:700;font-size:27px;line-height:1.12;text-transform:uppercase}
  .product-type{
    font-weight:700;font-size:50px;letter-spacing:3px;color:var(--teal);
    -webkit-text-stroke:2px var(--white);paint-order:stroke fill;margin-top:2px;
  }
  .product-name{
    font-family:"Alfa Slab One",Georgia,serif;font-size:96px;letter-spacing:4px;
    margin-top:40px;line-height:1;
  }
  .benefits{font-weight:700;font-size:26px;line-height:1.15;text-transform:uppercase;margin-top:40px}
  .volume{
    display:inline-block;margin-top:40px;background:var(--teal);
    font-weight:700;font-size:24px;padding:8px 28px;border-radius:8px;
  }

  /* ---------- back panel ---------- */
  .back{padding:0 38px;color:var(--ink-soft)}
  .back h2{font-size:27px;font-weight:700;color:var(--teal-dark);margin-top:26px}
  .intro{font-size:14px;line-height:1.3;margin-top:8px}
  .directions{
    margin-top:20px;border:2px dashed var(--teal);border-radius:14px;
    padding:26px 18px 14px;position:relative;
  }
  .directions h3{
    position:absolute;top:-16px;left:50%;transform:translateX(-50%);
    background:var(--magenta);color:var(--white);font-size:18px;letter-spacing:1px;
    padding:3px 26px;border-radius:8px;
  }
  .directions ol{list-style:none;font-size:14px;line-height:1.38}
  .section-title{
    text-align:center;color:var(--magenta);font-weight:700;font-size:17px;
    text-decoration:underline;margin-top:22px;
  }
  .ingredients{text-align:center;font-size:17px;margin-top:8px}
  .body-copy{font-size:14px;line-height:1.3;margin-top:8px}
</style>
</head>
<body>

  <section class="print-area front" aria-label="Front print">
    <div class="brand"><span>furbloom</span><span class="brand-dot"></span></div>
    <div class="scroll-frame" role="img" aria-label="Magenta panel framed by teal and white ornamental scrolls"></div>
    <div class="front-copy">
      <p class="claim">Super-Conditioning<br>and Nutrient</p>
      <p class="product-type">SHAMPOO</p>
      <p class="product-name">MILK</p>
      <p class="benefits">Moisture-Rich<br>Smooth and Silky</p>
      <p class="volume">1000 ml</p>
    </div>
  </section>

  <section class="print-area back" aria-label="Back print">
    <div class="brand"><span>furbloom</span><span class="brand-dot"></span></div>
    <h2>Super-Conditioning &amp; Nutrient Shampoo</h2>
    <p class="intro">is a specially formulated shampoo, rich in conditioners picked up from milk which subdivide and balance nutrition of pet's coat. More easier and better assimilate for coat from base to the end after using. With the help of minus-ion, the balancer of nutrition, rinses out quickly and completely to leave a soft, sparkling, and smooth coat. Safe and gentle enough to be used every day. Safe for even the most sensitive skin and coat, puppies, lactating bitches and cats.</p>

    <div class="directions">
      <h3>DIRECTIONS</h3>
      <ol>
        <li>a) Before shampooing, brush out pet's coat.</li>
        <li>b) Saturate dog's coat with lukewarm water.</li>
        <li>c) Dispense a small amount of shampoo into the palm of your hand.</li>
        <li>d) To clean coat, start at dog's head and work back towards the tail.</li>
        <li>e) Avoid getting shampoo into the dog's eyes and ears.</li>
        <li>f) Rinse coat several times with lukewarm water.</li>
        <li>g) Towel dry and gently comb or brush coat.</li>
      </ol>
    </div>

    <p class="section-title">ACTIVE INGREDIENTS:</p>
    <p class="ingredients">Hypochlorous Acid, Sodium Hypochlorite</p>

    <p class="section-title">USE PRECAUTIONS:</p>
    <p class="body-copy">Harmful if swallowed. Do not inhale. Discontinue use if irritation develops and contact your veterinarian. For animal use only. Not for human use. Keep out of reach of children. Do not decant into smaller containers. Not for injection. Always consult with a Veterinarian for systemic conditions.</p>

    <p class="section-title">STORAGE AND DISPOSAL</p>
    <p class="body-copy">Keep out of the touch of children. Replace Cap. Wrap in several layers of newspaper and discard in trash.</p>
  </section>

</body>
</html>
```